M Website

We need a website design for a construction plant company. You may use a combination of our photos and the stock images. See the logo for company colours. It also be of great value to see moving pictures like the ones on the link: https://www.quindellworks.co.za/copy-of-about-us. See our uploaded files for content.

Target Market(s)

Construction

Number of Pages Required

5+ page

```html
<!DOCTYPE html>
<html lang="en">
<head>
<meta charset="utf-8">
<title>Kestrel Logistics and Plant Hire</title>
<link href="https://fonts.googleapis.com/css2?family=Lato:wght@300;400;700;900&display=swap" rel="stylesheet">
<style>
:root{
  --yellow:#f2c31b;
  --yellow-deep:#e0ab12;
  --ink:#2b2b2b;
  --text:#444;
  --muted:#666;
  --dark:#1c1c1c;
  --panel:#2f2f2f;
  --bar:#3a3a3a;
  --footer:#2a2a2a;
  --white:#fff;
}
*{margin:0;padding:0;box-sizing:border-box}
html,body{width:1200px;height:2597px;overflow:hidden}
body{font-family:'Lato',sans-serif;color:var(--text);background:#fff;position:relative}
.abs{position:absolute}

/* hero */
.hero{position:absolute;left:0;top:0;width:1200px;height:525px;
  background:linear-gradient(160deg,#8a7256 0%,#b19472 35%,#9b7d5c 60%,#c4a57f 100%)}
.hero-shade{position:absolute;inset:0;background:linear-gradient(180deg,rgba(0,0,0,.35),rgba(0,0,0,0) 30%)}
.phone-top{position:absolute;right:187px;top:12px;color:#fff;font-weight:700;font-size:15px;display:flex;align-items:center;gap:8px}
.brand{position:absolute;left:187px;top:46px;display:flex;align-items:center;gap:10px;color:#fff;font-weight:900;font-size:26px;letter-spacing:1px}
.brand-dot{width:22px;height:22px;border-radius:50%;background:var(--yellow)}
.nav{position:absolute;right:187px;top:74px;display:flex;height:38px;align-items:center}
.nav a{color:#fff;font-size:13px;font-weight:700;text-decoration:none;padding:0 16px;height:38px;line-height:38px}
.nav a.active{background:var(--yellow);color:#222;padding:0 24px;clip-path:polygon(10% 0,90% 0,100% 100%,0 100%)}
.hero-title{position:absolute;left:0;width:1200px;top:250px;text-align:center;color:#fff;font-weight:700;font-size:38px;line-height:48px;text-shadow:0 2px 6px rgba(0,0,0,.4)}
.hero-title span{color:var(--yellow)}
.read-more{position:absolute;left:550px;top:362px;width:100px;text-align:center;color:#fff;font-size:11px;font-weight:700;padding-bottom:4px;border-bottom:2px solid var(--yellow)}
.chev{position:absolute;top:290px}

/* quote band */
.quote-band{position:absolute;left:187px;top:525px;width:826px;height:46px;background:var(--yellow);clip-path:polygon(0 0,100% 0,92% 100%,8% 100%);color:#fff;font-weight:700;font-size:14px;text-align:center;line-height:44px}
.quote-tab{position:absolute;left:533px;top:563px;width:134px;height:32px;background:#555;clip-path:polygon(12% 0,88% 0,100% 100%,0 100%);color:var(--yellow);font-size:11px;font-weight:700;text-align:center;line-height:26px}

/* overview */
.h-light{font-weight:400;font-size:24px;color:var(--ink)}
.rule{height:2px;background:var(--yellow)}
.body-s{font-size:11px;line-height:18px;color:var(--text)}
.photo{position:absolute}
.services{list-style:none;margin-top:4px}
.services li{font-size:11px;line-height:20px;padding-left:14px}
.services li::before{content:"•";margin-right:6px}
.delivering{position:absolute;right:187px;top:906px;text-align:right;font-size:14px;line-height:23px;color:var(--ink)}
.values-line{position:absolute;left:246px;top:1059px;width:710px;height:2px;background:var(--yellow)}
.value{position:absolute;top:1044px;width:160px;text-align:center;color:#555;font-size:14px;line-height:19px}
.value .tick{width:30px;height:30px;border-radius:50%;border:2px solid #444;background:#fff;margin:0 auto 12px;display:flex;align-items:center;justify-content:center}
.value b{color:var(--ink)}

/* mission */
.mission{position:absolute;left:0;top:1138px;width:1200px;height:320px;background:linear-gradient(120deg,#151515,#2a2a2a 60%,#1b1b1b)}
.tabs{position:absolute;left:236px;top:1186px;width:194px;border-right:3px solid var(--yellow)}
.tab{height:61px;line-height:61px;text-align:center;color:#fff;font-weight:700;font-size:15px;background:#2c2c2c;border-bottom:1px solid #1a1a1a}
.tab.on{color:var(--yellow);background:#222}
.mission h2{position:absolute;left:445px;top:1180px;color:#fff;font-size:23px;font-weight:700}
.mission .rule{position:absolute;left:445px;top:1217px;width:126px}
.mission p{position:absolute;left:445px;top:1230px;width:530px;color:#fff;font-size:11px;line-height:19px;font-weight:700}

/* projects */
.sec-title{position:absolute;left:0;width:1200px;text-align:center;font-weight:700;color:var(--ink)}
.filters{position:absolute;left:294px;top:1546px;width:614px;height:22px;display:flex;align-items:center;justify-content:space-between}
.arrow-box{width:30px;height:20px;background:#ccc;border-radius:3px}
.filter-list{display:flex;gap:12px;align-items:center;font-size:12px;color:#333}
.filter-list .all{background:var(--yellow);color:#fff;font-weight:700;padding:2px 6px;border-radius:3px}
.filter-list .hot{color:var(--yellow)}
.tile{position:absolute;top:1599px;width:196px;height:128px}
.tile-label{position:absolute;left:58px;top:1640px;color:#fff;font-weight:700;font-size:15px;line-height:22px}

/* testimonials */
.testi{position:absolute;left:0;top:1755px;width:1200px;height:303px;background:linear-gradient(180deg,var(--yellow),var(--yellow-deep))}
.testi h2{position:absolute;left:187px;top:1778px;color:#fff;font-size:38px;font-weight:900}
.testi .rule{position:absolute;left:210px;top:1829px;width:390px;background:#fff}
.client-name{position:absolute;left:340px;top:1851px;color:#fff;font-weight:700;font-size:13px}
.client-role{position:absolute;left:358px;top:1869px;color:var(--yellow);font-size:9px;filter:brightness(1.2)}
.avatar{position:absolute;top:1906px;width:74px;height:74px;border-radius:50%}
.v-line{position:absolute;left:661px;top:1888px;width:2px;height:109px;background:#fff}
.quote-text{position:absolute;left:727px;top:1880px;width:240px;color:#fff;font-weight:700;font-size:11px;line-height:19px}

/* cta */
.cta-title{position:absolute;left:0;width:1200px;text-align:center;font-weight:700;font-size:22px;line-height:37px;color:#333;top:2076px}
.cta-text{position:absolute;left:248px;top:2208px;width:500px;font-size:11px;line-height:23px;color:#555}
.cta-btn{position:absolute;left:804px;top:2208px;width:149px;height:59px;background:var(--yellow);color:#fff;font-size:14px;text-align:center;line-height:59px}

/* contact bar */
.contact-bar{position:absolute;left:0;top:2298px;width:1200px;height:75px;background:var(--bar);color:#fff}
.cb-item{position:absolute;top:15px;display:flex;gap:10px;font-size:9.5px;line-height:13px;font-weight:700}
.cb-btn{position:absolute;left:715px;top:15px;width:135px;height:45px;border:2px solid var(--yellow);color:#fff;font-size:11px;text-align:center;line-height:41px}
.social{position:absolute;left:942px;top:29px;display:flex;gap:12px}
.social span{width:16px;height:16px;border-radius:50%;background:#fff}

/* footer */
.footer{position:absolute;left:0;top:2373px;width:1200px;height:224px;background:var(--footer);color:#fff}
.f-h{position:absolute;top:36px;font-size:15px;font-weight:400}
.f-rule{position:absolute;top:60px;width:76px;height:2px;background:var(--yellow)}
.f-text{position:absolute;top:82px;font-size:11px;line-height:17px;font-weight:700}
.f-links{position:absolute;top:82px;font-size:11px;line-height:26px;font-weight:700}
</style>
</head>
<body>

<header class="hero" role="img" aria-label="Excavators and bulldozers working on an open earthworks construction site">
  <div class="hero-shade"></div>
</header>
<div class="phone-top">
  <svg width="16" height="16" viewBox="0 0 24 24" fill="#fff"><path d="M6.6 10.8a15 15 0 006.6 6.6l2.2-2.2a1 1 0 011-.25 11.4 11.4 0 003.6.57 1 1 0 011 1V20a1 1 0 01-1 1A17 17 0 013 4a1 1 0 011-1h3.5a1 1 0 011 1c0 1.25.2 2.45.57 3.6a1 1 0 01-.25 1z"/></svg>
  +27 (0) 87 555 0142
</div>
<div class="brand"><span class="brand-dot"></span>KESTREL</div>
<nav class="nav">
  <a class="active">ABOUT</a><a>SERVICE</a><a>PROJECTS</a><a>TEAM</a><a>CONTACT</a>
</nav>
<h1 class="hero-title">Transforming Our Clients Vision<br>Into <span>Reality</span></h1>
<div class="read-more">READ MORE</div>
<svg class="chev" style="left:24px" width="28" height="56" viewBox="0 0 28 56"><path d="M24 4L6 28l18 24" fill="none" stroke="#f2c31b" stroke-width="3"/></svg>
<svg class="chev" style="left:1148px" width="28" height="56" viewBox="0 0 28 56"><path d="M4 4l18 24L4 52" fill="none" stroke="#f2c31b" stroke-width="3"/></svg>

<div class="quote-band">We provide fast and affordable service for your projects. Hire us!</div>
<div class="quote-tab">GET QUOTES</div>

<!-- company overview -->
<h2 class="h-light abs" style="left:187px;top:618px">Company Overview</h2>
<div class="rule abs" style="left:187px;top:652px;width:190px"></div>
<p class="body-s abs" style="left:187px;top:670px;width:540px">Kestrel Logistics and Plant Hire (Pty) Ltd is a Black Woman owned Construction and Plant Hire company operating mainly from the Kestrel head office in Midrand (Ridgeview) Gauteng. Kestrel Logistics and Plant Hire (Pty) Ltd was established in 2014, and has worked in various municipal jurisdictions within South Africa.</p>
<div class="photo" style="left:786px;top:625px;width:227px;height:262px;background:linear-gradient(150deg,#f1f1ee,#d9b44a 55%,#8b6a3a)" role="img" aria-label="Excavator bucket digging at a building site"></div>
<div class="photo" style="left:187px;top:757px;width:225px;height:260px;background:linear-gradient(160deg,#3b3b3b,#6e6a62 55%,#9a8670)" role="img" aria-label="Machinery working through water on a roadworks site"></div>
<div class="abs" style="left:428px;top:798px;width:340px">
  <p class="body-s">Since inception, Kestrel Logistics and Plant Hire (Pty) Ltd has worked on a number of projects, acquiring a track record primarily in the following disciplines, amongst the company's offerings and/or services:</p>
  <ul class="services">
    <li>Roads &amp; Stormwater;</li>
    <li>Water Infrastructure;</li>
    <li>Sanitation Infrastructure and</li>
    <li>Housing</li>
  </ul>
</div>
<p class="delivering">delivering<br><b>high quality multidisciplinary engineering</b><br>and<br><b>construction projects</b></p>

<div class="values-line"></div>
<div class="value" style="left:336px"><div class="tick"><svg width="16" height="16" viewBox="0 0 16 16"><path d="M3 8.5l3 3 7-7" fill="none" stroke="#444" stroke-width="2"/></svg></div>WE ARE<br><b>PASSUIBATE</b></div>
<div class="value" style="left:519px"><div class="tick"><svg width="16" height="16" viewBox="0 0 16 16"><path d="M3 8.5l3 3 7-7" fill="none" stroke="#444" stroke-width="2"/></svg></div>HONEST &amp;<br><b>DEPENDABLE</b></div>
<div class="value" style="left:703px"><div class="tick"><svg width="16" height="16" viewBox="0 0 16 16"><path d="M3 8.5l3 3 7-7" fill="none" stroke="#444" stroke-width="2"/></svg></div>ALWAYS<br><b>INPROVING</b></div>

<!-- mission -->
<section class="mission" role="img" aria-label="Dark background of engineers reviewing plans"></section>
<div class="tabs">
  <div class="tab on">Mission Statement</div>
  <div class="tab">Why Choose Us?</div>
  <div class="tab on">Our Commitment</div>
  <div class="tab">Our Vision</div>
</div>
<div class="mission" style="background:none;height:0"></div>
<h2 class="abs" style="left:445px;top:1180px;color:#fff;font-size:23px;font-weight:700">OUR MISSION</h2>
<div class="rule abs" style="left:445px;top:1217px;width:126px"></div>
<p class="abs" style="left:445px;top:1230px;width:530px;color:#fff;font-size:11px;line-height:19px;font-weight:700">Kestrel Logistics and Plant Hire (Pty) Ltd is a Black Woman owned Construction and Plant Hire company operating mainly from the Kestrel head office in Midrand (Ridgeview) Gauteng. Kestrel Logistics and Plant Hire (Pty) Ltd was established in 2014, and has worked in various municipal jurisdictions within South Africa.</p>

<!-- projects -->
<h2 class="sec-title" style="top:1481px;font-size:22px">OUR PROJECTS</h2>
<div class="rule abs" style="left:540px;top:1518px;width:120px"></div>
<div class="filters">
  <span class="arrow-box"></span>
  <div class="filter-list">
    <span class="all">ALL</span><span>•</span><span>BUILDING</span><span>•</span><span class="hot">CONSTRUCTIONS</span><span>•</span><span>PROJECT PLANNIN</span>
  </div>
  <span class="arrow-box"></span>
</div>
<div class="tile" style="left:187px;background:linear-gradient(160deg,#3a3835,#5a4a40 60%,#8a3a2a)" role="img" aria-label="Powerline construction site with machinery at dusk"></div>
<div class="tile-label">Powerline<br>Construction</div>
<div class="tile" style="left:397px;background:linear-gradient(120deg,#f3f3f3,#d9d2cb 50%,#a0553a)" role="img" aria-label="Tall building under construction against white sky"></div>
<div class="tile" style="left:608px;background:linear-gradient(180deg,#e6e6e6,#6d6d6d 55%,#c7802f)" role="img" aria-label="Building frame with crane and lit floors"></div>
<div class="tile" style="left:818px;background:linear-gradient(150deg,#f1f1f1,#b8aea2 55%,#6e6458)" role="img" aria-label="Curved high-rise building under construction"></div>

<!-- testimonials -->
<section class="testi"></section>
<h2 class="abs" style="left:187px;top:1776px;color:#fff;font-size:38px;font-weight:900">WHAT OUR CLIENT SAYS</h2>
<div class="abs" style="left:210px;top:1829px;width:390px;height:2px;background:#fff"></div>
<div class="client-name">Daniel R. Pike</div>
<div class="abs" style="left:358px;top:1869px;color:#fff;font-size:9px;opacity:.8">Businessman</div>
<div class="avatar" style="left:188px;background:#5a4c44" role="img" aria-label="Client portrait"></div>
<div class="avatar" style="left:297px;background:#8a7260" role="img" aria-label="Client portrait"></div>
<div class="avatar" style="left:406px;background:#9b8066" role="img" aria-label="Client portrait"></div>
<div class="avatar" style="left:517px;background:#a88a6c" role="img" aria-label="Client portrait"></div>
<div class="v-line"></div>
<p class="quote-text">Lorem ipsum dolor sit amet, consectetur adipiscing elit. Duis ac ullamcorper ipsum. Nam dignissim vitae ligula in facilisis. In placerat vel mauris at hendrerit. Quisque scelerisque quis magna ut posuere. Vivamus in pharetra tellus.</p>

<!-- cta -->
<h2 class="cta-title">PROVIDING PERSONALIZED<br>AND<br>HIGH QUALITY SERVICES</h2>
<p class="cta-text">Etiam ut quam sed urna gravida varius id vel odio. Aliquam iaculis mauris odio, et pulvinar massa porttitor nec. Vestibulum felis diam, blandit vitae dignissim a, aliquam id felis. Curabitur efficitur laoreet libero, nec pellentesque arcu vestibulum vel.</p>
<div class="cta-btn">GET A QUOTE</div>

<!-- contact bar -->
<section class="contact-bar">
  <div class="cb-item" style="left:187px">
    <svg width="22" height="30" viewBox="0 0 22 30"><path d="M11 0a11 11 0 0111 11c0 8-11 19-11 19S0 19 0 11A11 11 0 0111 0z" fill="#f2c31b"/><circle cx="11" cy="11" r="4" fill="#3a3a3a"/></svg>
    <span>PO Box 418, Ridgeview, 1690<br>12 Acacia Lane, Ridgeview,<br>Midrand, 1692</span>
  </div>
  <div class="cb-item" style="left:472px;top:22px">
    <svg width="30" height="30" viewBox="0 0 24 24" fill="#f2c31b"><path d="M6.6 10.8a15 15 0 006.6 6.6l2.2-2.2a1 1 0 011-.25 11.4 11.4 0 003.6.57 1 1 0 011 1V20a1 1 0 01-1 1A17 17 0 013 4a1 1 0 011-1h3.5a1 1 0 011 1c0 1.25.2 2.45.57 3.6a1 1 0 01-.25 1z"/></svg>
    <span>+27 (0) 87 555 0142<br>info@kestrellogistics.co.za</span>
  </div>
  <div class="cb-btn">CONTACT US</div>
  <div class="social"><span></span><span></span><span></span></div>
</section>

<!-- footer -->
<footer class="footer">
  <div class="f-h" style="left:187px">ABOUT US</div>
  <div class="f-rule" style="left:187px"></div>
  <p class="f-text" style="left:187px;width:310px">Maecenas luctus accumsan ex, sed egestas elit semper vitae. Integer placerat massa a turpis egestas, id tincidunt nisl eleifend. Praesent vitae dictum dui. Donec blandit, augue sed aliquet volutpat, sem elit venenatis est,</p>
  <div class="f-h" style="left:570px">QUICK LINKS</div>
  <div class="f-rule" style="left:583px"></div>
  <div class="f-links" style="left:570px">Home<br>About<br>Service</div>
  <div class="f-links" style="left:720px">Projects<br>Team<br>Contact</div>
  <div class="f-h" style="left:871px">FREE STATE OFFICE</div>
  <div class="f-rule" style="left:895px"></div>
  <p class="f-text" style="left:871px;width:150px">Unit 7, Parkside Centre<br>Bloemfontein 9310</p>
</footer>

</body>
</html>
```